Digital Album Cover - Drifting Past Amber Harbor Lights (Piano & Cello)

HiI would like a digital album coverTitle: "Drifting Past Amber Harbor Lights (Piano & Cello)"Artist: "Rolf Dekker & The Osei Marit"

Requirements
Nice to have
• Original creativity
Should not have
• Copyrighted images

```html
<!DOCTYPE html>
<html lang="en">
<head>
<meta charset="utf-8">
<title>Drifting Past Amber Harbor Lights — Piano &amp; Cello</title>
<link rel="stylesheet" href="https://fonts.googleapis.com/css2?family=Gelasio:wght@500&family=Dancing+Script:wght@400&display=swap">
<style>
  :root {
    --page-bg: #21105c;
    --cover-top: #8d8aa3;
    --cover-mauve: #a05bb0;
    --cover-magenta: #8a3c9c;
    --cover-indigo: #2c1a62;
    --cover-deep: #15103f;
    --marble-light: #e4deef;
    --marble-lilac: #c78ee0;
    --title-ink: #ddd3ee;
    --script-gold: #a98b5c;
    --artist-ink: #e2dcef;
  }
  * { margin: 0; padding: 0; box-sizing: border-box; }
  html, body {
    width: 1200px;
    height: 850px;
    overflow: hidden;
    background: var(--page-bg);
  }
  .page {
    position: relative;
    width: 1200px;
    height: 850px;
    display: flex;
    align-items: center;
    justify-content: center;
  }
  .album-cover {
    position: relative;
    width: 600px;
    height: 600px;
    overflow: hidden;
    background: linear-gradient(
      to bottom,
      var(--cover-top) 0%,
      var(--cover-top) 22%,
      var(--cover-mauve) 50%,
      var(--cover-magenta) 62%,
      var(--cover-indigo) 74%,
      var(--cover-deep) 100%
    );
  }
  .cover-artwork {
    position: absolute;
    left: 66px;
    top: -40px;
    width: 420px;
    height: 380px;
    border-radius: 50%;
    background: radial-gradient(
      ellipse at 50% 40%,
      var(--marble-light) 0%,
      var(--marble-lilac) 48%,
      rgba(160, 91, 176, 0) 72%
    );
  }
  .cover-text {
    position: absolute;
    left: 0;
    right: 0;
    text-align: center;
  }
  .album-title {
    top: 392px;
    font-family: "Gelasio", Georgia, serif;
    font-weight: 500;
    font-size: 31px;
    letter-spacing: 0.2px;
    color: var(--title-ink);
  }
  .album-edition {
    top: 440px;
    font-family: "Dancing Script", cursive;
    font-size: 34px;
    letter-spacing: 1.5px;
    color: var(--script-gold);
  }
  .album-artist {
    top: 530px;
    font-family: "Gelasio", Georgia, serif;
    font-weight: 500;
    font-size: 15px;
    color: var(--artist-ink);
  }
</style>
</head>
<body>
  <main class="page">
    <section class="album-cover">
      <div class="cover-artwork" role="img" aria-label="Photograph of a white marble statue of an embracing figure, shown upside down and tinted lilac"></div>
      <h1 class="cover-text album-title">Drifting Past Amber Harbor Lights</h1>
      <p class="cover-text album-edition">piano &amp; cello</p>
      <p class="cover-text album-artist">Rolf Dekker &amp; The Osei Marit</p>
    </section>
  </main>
</body>
</html>
```